SnackNook!!! A Vending Machine Business Looking for an attractive website.

We are a vending machine business in Northern Michigan. We have changed our name and have rebranded our company. We would like an attractive website that shares who we are, what services we provide, the products we offer in our machines, along with a form businesses can fill out to see if they are a good fit for our company. I would like to have a Home Page, About SnackNook, Why Choose SnackNook?, Products & Services, Contact Us (With a Login Option), and a page with a questionnaire for thos interested in getting a FREE Vending Machine.

Target Market(s)

Businesses, Campgrounds, Schools, and many more in Northern Michigan

Industry/Entity Type

Vending Machines

Coding

Coded - Design and coding required

Number of Pages Required

5+ page

Requirements
Must have
• An inviting and enticing Home Page. I want to get my potential clients engaged in our website.
Nice to have
• Possibly background photos from Northern Michigan
Should not have
• A corporate feel. I do not want a boring website.

```html
<!DOCTYPE html>
<html lang="en">
<head>
<meta charset="utf-8">
<title>SnackNook – Crave. Vend. Repeat.</title>
<link href="https://fonts.googleapis.com/css2?family=Lato:wght@400;700;900&display=swap" rel="stylesheet">
<style>
:root{
  --navy:#1f1f5e;
  --green:#2d5a27;
  --green-dark:#284f23;
  --mint:#e5f4df;
  --ink:#111;
  --white:#fff;
  --black:#0b0b0b;
}
*{box-sizing:border-box;margin:0;padding:0}
html,body{width:1200px;height:3294px;overflow:hidden}
body{font-family:'Lato',sans-serif;color:var(--ink);background:var(--white);position:relative}
.abs{position:absolute}
a{color:inherit;text-decoration:none}

/* header */
.site-header{position:absolute;top:0;left:0;width:1200px;height:94px;background:var(--white)}
.brand{position:absolute;left:113px;top:28px;display:flex;align-items:center;gap:10px;font-size:32px;font-weight:900;color:var(--navy)}
.brand .dot{width:22px;height:22px;background:var(--green);border-radius:50%}
.location{position:absolute;left:670px;top:22px;display:flex;gap:14px;align-items:center}
.location small{display:block;font-size:14px;color:var(--green);font-weight:700}
.location span{font-size:16px;font-weight:700;color:#222}
.btn-login{position:absolute;left:980px;top:24px;width:110px;height:47px;border-radius:24px;background:var(--green);color:var(--white);font-size:18px;display:flex;align-items:center;justify-content:center}

.main-nav{position:absolute;top:94px;left:0;width:1200px;height:57px;background:var(--green)}
.main-nav .call-panel{position:absolute;left:898px;top:0;width:302px;height:57px;background:var(--navy)}
.main-nav ul{list-style:none}
.main-nav li{position:absolute;top:20px;font-size:15px;color:var(--white)}
.call{position:absolute;left:898px;top:10px;display:flex;align-items:center;gap:14px;color:var(--white)}
.call .ring{width:34px;height:34px;border-radius:50%;background:var(--white);display:flex;align-items:center;justify-content:center}
.call small{display:block;font-size:14px}
.call span{font-size:17px}

/* hero */
.hero{position:absolute;top:151px;left:0;width:1200px;height:512px;background:linear-gradient(90deg,#2b3550 0%,#46434a 35%,#3a3a3d 65%,#26282d 100%)}
.hero-shade{position:absolute;inset:0;background:rgba(15,15,25,.35)}
.hero h1{position:absolute;top:140px;width:100%;text-align:center;font-weight:400;color:var(--white);font-size:30px}
.hero h2{position:absolute;top:198px;width:100%;text-align:center;font-weight:400;color:var(--white);font-size:34px}
.btn-pill{position:absolute;height:48px;border-radius:24px;display:flex;align-items:center;justify-content:center;font-size:19px}
.btn-solid{background:var(--white);color:var(--navy)}
.btn-outline{border:2px solid var(--white);color:var(--white)}

/* products */
.section-title{position:absolute;width:100%;text-align:center;font-size:42px;font-weight:700;color:var(--navy)}
.section-title em{font-style:normal;color:var(--green)}
.product-card{position:absolute;top:790px;width:268px;height:332px;border:2px solid #e3e3e3;border-radius:16px;background:var(--white)}
.product-card .photo{position:absolute;left:12px;top:13px;width:244px;height:250px;border-radius:12px}
.product-card p{position:absolute;top:288px;width:100%;text-align:center;color:var(--green);font-size:19px}
.arrow{position:absolute;top:936px;width:25px;height:25px;border-radius:50%;background:var(--green);display:flex;align-items:center;justify-content:center}

/* about */
.about{position:absolute;top:1194px;left:0;width:1200px;height:658px;background:var(--mint)}
.about .thumb{position:absolute;width:187px;height:108px}
.about-text{position:absolute;left:255px;top:186px;width:690px;text-align:center;font-size:15px;line-height:31px;color:#1a1a1a}
.btn-dark{position:absolute;height:50px;border-radius:25px;background:var(--navy);color:var(--white);font-size:17px;display:flex;align-items:center;justify-content:center}

/* why */
.why-intro{position:absolute;top:1975px;left:190px;width:820px;text-align:center;font-size:15px;font-weight:700;line-height:27px}
.why-card{position:absolute;top:2097px;width:225px;height:296px;border-radius:14px;color:var(--white);text-align:center;padding:28px 16px 0}
.why-card.green{background:var(--green)}
.why-card.navy{background:var(--navy)}
.why-card h3{font-size:17px;font-weight:700;line-height:29px;margin-bottom:6px}
.why-card p{font-size:12.5px;line-height:28px}
.why-card a{position:absolute;bottom:32px;left:0;width:100%;font-size:15px;font-weight:700;text-decoration:underline}

/* cta */
.cta{position:absolute;top:2475px;left:0;width:1200px;height:417px;background:linear-gradient(160deg,#1f2a5a 0%,#243e4c 45%,#2d5a27 100%);color:var(--white);text-align:center}
.cta h2{position:absolute;top:50px;width:100%;font-size:40px;line-height:62px;font-weight:700}
.cta p{position:absolute;top:188px;width:100%;font-size:17px;line-height:34px;font-weight:700}

/* footer */
.site-footer{position:absolute;top:2892px;left:0;width:1200px;height:402px;background:var(--black);color:var(--white)}
.footer-brand{position:absolute;left:113px;top:100px;display:flex;align-items:center;gap:12px;font-size:40px;font-weight:900}
.footer-brand .dot{width:26px;height:26px;border-radius:50%;background:var(--white)}
.social{position:absolute;top:205px;width:32px;height:32px;border-radius:50%;background:var(--white)}
.col-title{position:absolute;top:76px;font-size:20px;font-weight:700}
.link-list{position:absolute;top:118px;list-style:none;font-size:15px}
.link-list li{height:34.5px;display:flex;align-items:center;gap:10px}
.contact-row{position:absolute;left:903px;display:flex;gap:14px;align-items:center;font-size:15px;line-height:27px}
.contact-row .ic{width:32px;height:32px;border-radius:50%;background:var(--white);display:flex;align-items:center;justify-content:center;flex:none}
.divider{position:absolute;left:109px;top:322px;width:977px;height:1px;background:#bbb}
.copyright{position:absolute;top:358px;width:100%;text-align:center;font-size:15px;font-weight:700}
</style>
</head>
<body>

<header class="site-header">
  <div class="brand"><span class="dot"></span>SnackNook</div>
  <div class="location">
    <svg width="32" height="34" viewBox="0 0 32 34" fill="none" stroke="#555" stroke-width="1.6"><path d="M16 3a8 8 0 0 0-8 8c0 6 8 14 8 14s8-8 8-14a8 8 0 0 0-8-8z"/><circle cx="16" cy="11" r="3"/><path d="M6 22l-4 9h28l-4-9"/></svg>
    <div><small>Location</small><span>SnackNook, Northern Michigan</span></div>
  </div>
  <a class="btn-login" href="#">Login</a>
</header>

<nav class="main-nav">
  <div class="call-panel"></div>
  <ul>
    <li style="left:112px">Home</li>
    <li style="left:204px">About SnackNook</li>
    <li style="left:376px">Why Choose SnackNook?</li>
    <li style="left:608px">Products &amp; Services</li>
    <li style="left:794px">Contact Us</li>
  </ul>
  <div class="call">
    <span class="ring"><svg width="16" height="16" viewBox="0 0 24 24" fill="none" stroke="#1f1f5e" stroke-width="2"><path d="M5 3h4l2 5-3 2a12 12 0 0 0 6 6l2-3 5 2v4a2 2 0 0 1-2 2A17 17 0 0 1 3 5a2 2 0 0 1 2-2z"/></svg></span>
    <div><small>Call Us</small><span>+1 555 014 2290</span></div>
  </div>
</nav>

<section class="hero" role="img" aria-label="Woman choosing a snack from a lit vending machine">
  <div class="hero-shade"></div>
  <h1>SnackNook: Crave. Vend. Repeat.</h1>
  <h2>Elevating Snacking, One Vend at a Time</h2>
  <a class="btn-pill btn-solid" href="#" style="left:359px;top:286px;width:156px">Get Started</a>
  <a class="btn-pill btn-outline" href="#" style="left:554px;top:285px;width:289px">Get a FREE Vending Machine</a>
</section>

<h2 class="section-title" style="top:710px">Our <em>Products</em></h2>
<div class="arrow" style="left:40px"><svg width="10" height="12" viewBox="0 0 10 12"><path d="M7 1L2 6l5 5" stroke="#fff" stroke-width="2" fill="none"/></svg></div>
<div class="arrow" style="left:1128px"><svg width="10" height="12" viewBox="0 0 10 12"><path d="M3 1l5 5-5 5" stroke="#fff" stroke-width="2" fill="none"/></svg></div>
<article class="product-card" style="left:130px">
  <div class="photo" role="img" aria-label="Snack vending machine stocked with chips" style="background:linear-gradient(135deg,#1d2a3c,#5a6a78 50%,#2b3b4d)"></div>
  <p>Itaque earum rerum</p>
</article>
<article class="product-card" style="left:467px">
  <div class="photo" role="img" aria-label="Row of drink vending machines" style="background:linear-gradient(90deg,#6d7f93,#1f3f9a 45%,#2a48a8 70%,#c8403a)"></div>
  <p>Taque earum rerum</p>
</article>
<article class="product-card" style="left:801px">
  <div class="photo" role="img" aria-label="Hand taking a coffee cup from a machine" style="background:linear-gradient(135deg,#e7e4e1,#b9b1ab 55%,#2b2622)"></div>
  <p>Aue earum rerum</p>
</article>

<section class="about">
  <div class="thumb" role="img" aria-label="Small northern Michigan town street" style="left:133px;top:56px;background:linear-gradient(#8fb4d8,#8a8c6e 60%,#6a5a4a)"></div>
  <div class="thumb" role="img" aria-label="Vending machines in a dark lounge" style="left:860px;top:62px;background:linear-gradient(90deg,#2a2420,#6a5848 50%,#3a2a22)"></div>
  <div class="thumb" role="img" aria-label="Smiling customer at a vending machine" style="left:21px;top:256px;background:linear-gradient(90deg,#7a2a2a,#b07a5a 50%,#5a4a40)"></div>
  <div class="thumb" role="img" aria-label="Hand selecting an item on a vending keypad" style="left:975px;top:256px;background:linear-gradient(90deg,#3a4a6a,#c8b8a8 55%,#2a2a2a)"></div>
  <div class="thumb" role="img" aria-label="Vending machines in a shopping mall" style="left:188px;top:464px;background:linear-gradient(90deg,#d8d2c8,#b84a3a 50%,#e8e2d8)"></div>
  <div class="thumb" role="img" aria-label="Close view of a stocked snack machine" style="left:804px;top:464px;background:linear-gradient(90deg,#1f3050,#c07a3a 45%,#8a8a92)"></div>
  <h2 class="section-title" style="top:118px">About <em>SnackNook</em></h2>
  <div class="about-text">
    <p>At SnackNook, we don't just vend snacks—we curate cravings. Our customized vending solutions bring flavor, convenience, and community to Northern Michigan. Whether you're reaching for a mid-morning snack, a refreshing beverage, or a satisfying breakfast burrito, SnackNook delivers delight with every bite.</p>
    <p style="margin-top:31px">We're not just about vending machines; we're your culinary companions, your flavor curators, and your secret stash of happiness.We're the ones who believe that a vending machine isn't just a metal box; it's a portal to delight.</p>
  </div>
  <a class="btn-dark" href="#" style="left:519px;top:455px;width:162px">Read More</a>
</section>

<h2 class="section-title" style="top:1902px">Why <em>Choose Us</em></h2>
<p class="why-intro">At SnackNook, we're more than vending machines; we're flavor architects, communityconnectors, and taste trail-blazers. Imagine a world where every snack is an adventure, everysip a celebration. That's the SnackNook promise—a symphony of taste, convenience, andcamaraderie.</p>

<article class="why-card green" style="left:111px">
  <h3>Local Love</h3>
  <p>We celebrate the heart of Michigan by partnering with local legends. Say hello to Birchwood Jerky and Pinecone Potato Chips—our hometown heroes.</p>
  <a href="#">Read More</a>
</article>
<article class="why-card navy" style="left:362px">
  <h3>Unleash Your Cravings</h3>
  <p>SnackNook isn't bound by corporate ties. We're the rebels of the vending world. Craving a bag of crispy, kettle-cooked chips? Done.</p>
  <a href="#">Read More</a>
</article>
<article class="why-card green" style="left:614px">
  <h3>Quality<br>Meets Convenience</h3>
  <p>Imagine this: You're mid-meet-ing, and your stomach growls. Fear not! SnackNook's machines offer top-notch snacks and beverages</p>
  <a href="#">Read More</a>
</article>
<article class="why-card navy" style="left:866px">
  <h3>Pandemic-Proof<br>&amp; Recession-Ready</h3>
  <p>Life throws curveballs, but SnackNook stands strong. Our vending machines are the unsung heroes of resilience.</p>
  <a href="#">Read More</a>
</article>

<section class="cta" role="img" aria-label="Aerial view of northern Michigan forest under a blue and green tint">
  <h2>Ready to experience the SnackNook<br>difference?</h2>
  <p>Sign up now and let's connect. Taste the future of snacking firsthand! Contact us today<br>and explore how our vending magic can elevate your space.</p>
  <a class="btn-pill btn-solid" href="#" style="left:513px;top:295px;width:175px;font-size:17px">Contact Us Today</a>
</section>

<footer class="site-footer">
  <div class="footer-brand"><span class="dot"></span>SnackNook</div>
  <span class="social" style="left:108px"></span>
  <span class="social" style="left:166px"></span>
  <span class="social" style="left:224px"></span>
  <span class="social" style="left:282px"></span>

  <h4 class="col-title" style="left:462px">Quick Links</h4>
  <ul class="link-list" style="left:462px">
    <li><svg width="13" height="12" viewBox="0 0 13 12"><path d="M1 6h10M7 2l4 4-4 4" stroke="#fff" stroke-width="2" fill="none"/></svg>Home</li>
    <li><svg width="13" height="12" viewBox="0 0 13 12"><path d="M1 6h10M7 2l4 4-4 4" stroke="#fff" stroke-width="2" fill="none"/></svg>About</li>
    <li><svg width="13" height="12" viewBox="0 0 13 12"><path d="M1 6h10M7 2l4 4-4 4" stroke="#fff" stroke-width="2" fill="none"/></svg>Product</li>
    <li><svg width="13" height="12" viewBox="0 0 13 12"><path d="M1 6h10M7 2l4 4-4 4" stroke="#fff" stroke-width="2" fill="none"/></svg>Why choose us</li>
    <li><svg width="13" height="12" viewBox="0 0 13 12"><path d="M1 6h10M7 2l4 4-4 4" stroke="#fff" stroke-width="2" fill="none"/></svg>Contact Us</li>
  </ul>

  <h4 class="col-title" style="left:677px">Help Links</h4>
  <ul class="link-list" style="left:677px">
    <li><svg width="13" height="12" viewBox="0 0 13 12"><path d="M1 6h10M7 2l4 4-4 4" stroke="#fff" stroke-width="2" fill="none"/></svg>FAQ</li>
    <li><svg width="13" height="12" viewBox="0 0 13 12"><path d="M1 6h10M7 2l4 4-4 4" stroke="#fff" stroke-width="2" fill="none"/></svg>Terms of use</li>
    <li><svg width="13" height="12" viewBox="0 0 13 12"><path d="M1 6h10M7 2l4 4-4 4" stroke="#fff" stroke-width="2" fill="none"/></svg>Privacy Policy</li>
    <li><svg width="13" height="12" viewBox="0 0 13 12"><path d="M1 6h10M7 2l4 4-4 4" stroke="#fff" stroke-width="2" fill="none"/></svg>Support Links</li>
    <li><svg width="13" height="12" viewBox="0 0 13 12"><path d="M1 6h10M7 2l4 4-4 4" stroke="#fff" stroke-width="2" fill="none"/></svg>Conditions</li>
  </ul>

  <h4 class="col-title" style="left:903px">Contact Us</h4>
  <div class="contact-row" style="top:122px">
    <span class="ic"><svg width="14" height="18" viewBox="0 0 14 18"><path d="M7 1a6 6 0 0 0-6 6c0 4.5 6 10 6 10s6-5.5 6-10a6 6 0 0 0-6-6z" fill="#0b0b0b"/><circle cx="7" cy="7" r="2" fill="#fff"/></svg></span>
    <div>SnackNook<br>United States</div>
  </div>
  <div class="contact-row" style="top:192px">
    <span class="ic"><svg width="16" height="16" viewBox="0 0 24 24" fill="none" stroke="#0b0b0b" stroke-width="2.4"><path d="M5 3h4l2 5-3 2a12 12 0 0 0 6 6l2-3 5 2v4a2 2 0 0 1-2 2A17 17 0 0 1 3 5a2 2 0 0 1 2-2z"/></svg></span>
    <div>+1 555 014 2290</div>
  </div>
  <div class="contact-row" style="top:243px">
    <span class="ic"><svg width="16" height="12" viewBox="0 0 16 12"><rect x="1" y="1" width="14" height="10" fill="#0b0b0b"/><path d="M1 1l7 6 7-6" stroke="#fff" stroke-width="1.4" fill="none"/></svg></span>
    <div>hello@snacknook.com</div>
  </div>

  <div class="divider"></div>
  <p class="copyright">Copyrights@2024.SnackNook.All Rights Reserved</p>
</footer>

</body>
</html>
```